Colin Vesk Personal Card

I am looking for a personal card that has my contact information on the front and then the url for my website on the back. I am a fan of minimal, modern design, but am very open minded to other styles. Both portrait and landscape designs are acceptable. The only other specification that I have is that some sort of graphic of a raven is present somewhere on the card (my last name 'Vesk' means raven in German).
Industry/Entity Type
Landscape
Contact Information for Business Card
Colin Vesk
508.641.2093
colintvesk@postvale.com
colintvesk.com
Colors
Designer to choose colors to be used in the design.
Requirements
Must have
- Raven on some part of the card

```html
<!DOCTYPE html>
<html lang="en">
<head>
<meta charset="utf-8">
<title>Colin Vesk Personal Card</title>
<link rel="stylesheet" href="https://fonts.googleapis.com/css2?family=Oswald:wght@500;600&family=Roboto:wght@400&display=swap">
<style>
  :root {
    --backdrop: #3a3a3a;
    --card-black: #050505;
    --card-white: #f4f4f4;
    --ink: #1a1a1a;
    --paper-ink: #ffffff;
  }
  * { margin: 0; padding: 0; box-sizing: border-box; }
  html, body {
    width: 1200px;
    height: 1200px;
    overflow: hidden;
    background: var(--backdrop);
  }
  .sheet {
    width: 1200px;
    height: 1200px;
    display: flex;
    flex-direction: column;
    align-items: center;
    justify-content: center;
    gap: 70px;
  }
  .card {
    width: 760px;
    height: 434px;
    position: relative;
    box-shadow: 0 14px 40px rgba(0,0,0,0.45);
  }
  .card--back {
    background: var(--card-black);
    display: flex;
    flex-direction: column;
    align-items: center;
    justify-content: center;
  }
  .brand-dot {
    width: 56px;
    height: 56px;
    border-radius: 50%;
    background: var(--paper-ink);
    margin-bottom: 24px;
  }
  .back-name {
    font-family: "Oswald", sans-serif;
    font-weight: 600;
    font-size: 32px;
    letter-spacing: 9px;
    line-height: 1;
    color: var(--paper-ink);
    text-transform: uppercase;
  }
  .card--front {
    background: linear-gradient(160deg, #ffffff 0%, var(--card-white) 60%, #e6e6e6 100%);
    display: flex;
    align-items: center;
    justify-content: center;
    gap: 20px;
  }
  .identity {
    text-align: right;
  }
  .identity-name {
    font-family: "Oswald", sans-serif;
    font-weight: 600;
    font-size: 44px;
    letter-spacing: 11px;
    line-height: 1;
    color: var(--ink);
    text-transform: uppercase;
  }
  .identity-phone {
    font-family: "Oswald", sans-serif;
    font-weight: 500;
    font-size: 18px;
    letter-spacing: 8px;
    line-height: 1;
    color: var(--ink);
    margin-top: 8px;
  }
  .divider {
    width: 2px;
    height: 88px;
    background: var(--ink);
  }
  .contact-list {
    list-style: none;
    font-family: "Roboto", sans-serif;
    font-size: 17px;
    color: var(--ink);
    line-height: 1.55;
  }
  .contact-list li {
    display: flex;
    align-items: center;
    gap: 8px;
  }
  .contact-icon {
    width: 12px;
    height: 12px;
    flex: none;
  }
</style>
</head>
<body>
  <main class="sheet">
    <section class="card card--back">
      <div class="brand-dot"></div>
      <p class="back-name">Colin Vesk</p>
    </section>

    <section class="card card--front">
      <div class="identity">
        <h1 class="identity-name">Colin Vesk</h1>
        <p class="identity-phone">508.641.2093</p>
      </div>
      <div class="divider"></div>
      <ul class="contact-list">
        <li>
          <svg class="contact-icon" viewBox="0 0 12 12"><path d="M2.5 1 L4.5 1 L5 3.5 L3.8 4.3 Q4.8 6.8 7.7 8.2 L8.5 7 L11 7.5 L11 9.5 Q10.5 11 8.5 10.8 Q2 9.5 1 3 Q1 1.3 2.5 1 Z" fill="#1a1a1a"/></svg>
          508.641.2093
        </li>
        <li>
          <svg class="contact-icon" viewBox="0 0 12 12"><rect x="1" y="2.5" width="10" height="7" fill="none" stroke="#1a1a1a" stroke-width="1.2"/><path d="M1 2.5 L6 6.5 L11 2.5" fill="none" stroke="#1a1a1a" stroke-width="1.2"/></svg>
          colintvesk@postvale.com
        </li>
        <li>
          <svg class="contact-icon" viewBox="0 0 12 12"><circle cx="6" cy="6" r="5" fill="none" stroke="#1a1a1a" stroke-width="1.2"/><ellipse cx="6" cy="6" rx="2.2" ry="5" fill="none" stroke="#1a1a1a" stroke-width="1"/><line x1="1" y1="6" x2="11" y2="6" stroke="#1a1a1a" stroke-width="1"/></svg>
          colintvesk.com
        </li>
      </ul>
    </section>
  </main>
</body>
</html>
```